Business Card Design Project

We need a business card designed for a new Luxury Custom Homebuilding company based in Arizona. We previous were called "Belcrest Custom Homes" but want to start using "Belcrest Custom Homes" We want the message to communicate high end, luxury and cutting-edge. We like the blue, white and black color scheme.
Belcrest Custom Homes
Marcus T. Halloway
Chief Executive Officer
Office: 480-555-0142
Mobile: 480-555-0178
email: marc@belcrestcustom-example.com
web adress: www.BelcrestCustom-example.com
Updates
We have made a change to our website address and email address based on recieving feedback from a nmber of individuals. The feedback was web address and email address was to long. Therefore we have made a change. The new web adress and email adress are the following.
www.BelcrestCustom-example.com
marc@belcrestcustom-example.com
Also I decided against using in yellow. I like the colors blue,black, white and maybe gray.
Target Market(s)
Our target market is the wealthy individuals looking for a luxury high-end custom home.
Industry/Entity Type
Business
Look and feel

```html
<!DOCTYPE html>
<html lang="en">
<head>
<meta charset="utf-8">
<title>Belcrest Custom Homes – Business Card</title>
<link rel="stylesheet" href="https://fonts.googleapis.com/css2?family=Montserrat:wght@400;500;700;800&display=swap">
<style>
  :root {
    --backdrop: #3a3a3c;
    --card: #141416;
    --card-edge: #222226;
    --white: #f4f5f7;
    --grey: #a9abb0;
    --blue: #3f8fd8;
  }
  * { box-sizing: border-box; margin: 0; padding: 0; }
  html, body { width: 1200px; height: 715px; overflow: hidden; }
  body {
    background: var(--backdrop);
    font-family: "Montserrat", Arial, sans-serif;
    position: relative;
  }
  .card {
    position: absolute;
    top: 200px;
    width: 525px;
    height: 300px;
    background: var(--card);
    border: 1px solid var(--card-edge);
    border-radius: 3px;
    box-shadow: 0 14px 30px rgba(0,0,0,.45);
  }
  .card--front { left: 50px; }
  .card--back { left: 625px; }

  .wordmark {
    display: flex;
    align-items: center;
    gap: 12px;
    color: var(--white);
    font-weight: 800;
    font-size: 30px;
    letter-spacing: -0.5px;
    line-height: 1.05;
    white-space: nowrap;
  }
  .wordmark .mark-square {
    width: 14px; height: 14px;
    background: var(--blue);
    flex: none;
  }

  .card--front .brand-block {
    position: absolute; left: 50px; top: 100px;
    display: flex; flex-direction: column; align-items: flex-end;
  }
  .card--front .wordmark { font-size: 32px; }
  .card--front .website {
    margin-top: 18px;
    color: var(--blue); font-size: 13px; font-weight: 500;
    white-space: nowrap;
  }

  .card--back .wordmark { position: absolute; left: 34px; top: 40px; font-size: 26px; }

  .address {
    position: absolute; left: 34px; top: 140px;
    font-style: normal;
    font-size: 12px; line-height: 1.6; color: var(--grey);
    white-space: nowrap;
  }
  .label { color: var(--blue); }

  .person {
    position: absolute; left: 232px; top: 140px;
  }
  .person .name {
    color: var(--blue); font-size: 16px; font-weight: 500;
    letter-spacing: 0.8px; text-transform: uppercase;
    white-space: nowrap;
  }
  .person .title { color: var(--grey); font-size: 12px; margin-top: 2px; }
  .contacts {
    list-style: none; margin-top: 16px;
    font-size: 12px; line-height: 1.65; color: var(--grey);
  }
  .contacts li { white-space: nowrap; }
  .contacts .label { display: inline-block; width: 48px; }
</style>
</head>
<body>
  <section class="card card--front">
    <div class="brand-block">
      <div class="wordmark"><span class="mark-square"></span>Belcrest Custom Homes</div>
      <div class="website">www.BelcrestCustom-example.com</div>
    </div>
  </section>

  <section class="card card--back">
    <div class="wordmark"><span class="mark-square"></span>Belcrest Custom Homes</div>

    <address class="address">
      <span class="label">Address:</span><br>
      2210 N. Larkspur Drive,<br>
      Suite 88 Mesa, AZ 85200
    </address>

    <div class="person">
      <div class="name">Marcus T. Halloway</div>
      <div class="title">Chief Executive Officer</div>
      <ul class="contacts">
        <li><span class="label">Office:</span>480-555-0142</li>
        <li><span class="label">Mobile:</span>480-555-0178</li>
        <li><span class="label">Email:</span>marc@belcrestcustom-example.com</li>
      </ul>
    </div>
  </section>
</body>
</html>
```